6x11 Postcard for Moving Company

Must have company logo and the company slogan underneath: "The Moving Company You Can Trust And Rely On!". Must have company phone number: 858-555-0142. Must have company email, website and address:
info@haul-pivot.com
www.haul-pivot.com
4127 Penwick Lane, Suite B1,
San Diego, CA 92177
Must have company licenses listed in the following format:
CAL-T# 574318 | CA# 208751 | MC# 362940 | USDOT# 7140829

Must include the following services:
Packing - Moving - Unpacking
Loading - Unloading
Storage In Transit
Long Term Storage
Local - Long Distance
Residential - Commercial
Licensed - Insured
Free Onsite and Video Estimates

And please include the following text above or below the phone number: "Call For FREE Friendly Estimates and Advice!"

Target Market(s)

New Homes that go on sale and Home that were sold and in pending status.

Industry/Entity Type

Moving Company

Colors

Designer to choose colors to be used in the design.

Requirements
Must have
• A photo of a family on the front of the postcard. Must be looking like a real photo of the actual owner of the company with wife and 2 kids (not just a basic stock family photo). Must have Qorvix Assurance Logo and the text "Qorvix Assured". Must say/include 5 star rating on Tarnly, Qorvix, Nestplanner, Chatterwall, Pinbrook. Must include FQC A+ Accreditation Logo. Must include the Certified HaulSure Logo (see attached) and the Golden Haul Expert badege. Must have a Book Online Option. Must leave space for FMDA permit for postage. Must include the following deals: $250 Off Long Distance Moves, $50 Off Local Moves, Free Boxes (*call for details), 1 Month Storage Free. (in smaller text must say: *Offers can not be combined with other offers)

```html
<!DOCTYPE html>
<html lang="en">
<head>
<meta charset="utf-8">
<title>Haul Pivot Postcard</title>
<link rel="stylesheet" href="https://fonts.googleapis.com/css2?family=Oswald:wght@600;700&family=Roboto+Condensed:wght@400;700&family=Open+Sans:wght@400;600;700;800&display=swap">
<style>
:root{
  --navy:#111a3a;
  --navy-deep:#0b1230;
  --navy-soft:#1b2552;
  --red:#e8202a;
  --white:#ffffff;
  --grey:#eaebed;
  --ink:#3a3d45;
  --gold:#f7b81b;
  --green:#2fa84f;
  --orange:#f0a53a;
  --stage:#cfdbe0;
}
*{margin:0;padding:0;box-sizing:border-box}
html,body{width:1120px;height:1200px;overflow:hidden}
body{background:var(--stage);position:relative;font-family:"Open Sans",sans-serif}
.card{position:absolute;left:36px;width:1040px;height:568px;overflow:hidden;background:var(--white);box-shadow:0 3px 10px rgba(0,0,0,.35)}
.card--front{top:22px}
.card--back{top:609px}
.layer{position:absolute;left:0;top:0;width:1040px;height:568px}
.abs{position:absolute}

.brand{position:absolute;left:30px;top:46px;width:150px;text-align:center}
.brand__mark{display:block;width:58px;height:58px;margin:0 auto 12px;background:var(--red)}
.brand__name{font-family:"Oswald",sans-serif;font-weight:700;font-size:29px;line-height:1;color:var(--white);letter-spacing:.5px}

.contact{position:absolute}
.contact__lead{font-family:"Roboto Condensed",sans-serif;font-weight:700;font-size:24px;line-height:26px;color:var(--red);margin-bottom:6px}
.contact__row{display:flex;align-items:flex-start;font-size:16.5px;line-height:22.5px;color:var(--white)}
.contact__icon{width:13px;height:13px;margin:4px 9px 0 0;flex:none}

.slogan{position:absolute;left:24px;top:212px;font-family:"Oswald",sans-serif;font-weight:700;line-height:1}
.slogan__top{font-size:51px;color:var(--navy);letter-spacing:.2px}
.slogan__bottom{font-size:41px;color:var(--red);margin-top:6px;letter-spacing:.1px}

.tab{position:absolute;font-weight:800;font-size:20px;color:var(--white);letter-spacing:.3px}

.services{position:absolute;top:381px;list-style:none}
.services li{display:flex;align-items:center;height:27.5px;font-size:18.5px;color:var(--ink)}
.tick{width:16px;height:16px;margin-right:8px;flex:none}

.licenses{position:absolute;color:var(--red);white-space:nowrap}

.offer-band{position:absolute;left:600px;top:336px;width:440px;text-align:center}
.offer-band__main{font-family:"Roboto Condensed",sans-serif;font-weight:700;font-size:19px;color:var(--red);padding-left:40px}
.offer-band__note{font-family:"Roboto Condensed",sans-serif;font-size:14px;color:var(--white);margin-top:4px;padding-left:40px}

.ribbon{position:absolute;left:890px;top:12px;width:140px;text-align:center;color:var(--white);font-weight:700}
.ribbon__big{font-size:18px;line-height:22px;font-weight:800}
.ribbon__small{font-size:14px;line-height:16px}
.ribbon__stars{font-size:9px;letter-spacing:4px;margin:4px 0 6px}

.reviews{position:absolute;border:2px solid var(--navy);border-radius:12px;background:var(--white);display:flex;flex-direction:column;justify-content:center;gap:6px;padding:0 10px}
.reviews__row{display:flex;align-items:center;gap:10px;font-weight:700;color:var(--navy)}
.reviews__seal{display:inline-block;background:#1d5fa6;border-radius:2px}
.stars{position:absolute;color:var(--gold);letter-spacing:1px;line-height:1}

.assured{position:absolute;display:flex;align-items:center;gap:7px}
.assured__shield{flex:none}
.assured__name{font-weight:800;color:#222;line-height:1.05}
.assured__sub{font-size:6px;line-height:8px;color:#555;margin-top:3px}

.about{position:absolute;left:20px;top:246px;width:560px;font-size:15px;line-height:18.4px;color:var(--ink)}
.stamp{position:absolute;left:923px;top:22px;width:92px;height:112px;border:2px solid #111}
</style>
</head>
<body>

<!-- FRONT -->
<section class="card card--front">
  <svg class="layer" viewBox="0 0 1040 568" aria-hidden="true">
    <defs>
      <linearGradient id="navyFade" x1="0" y1="0" x2="0" y2="1">
        <stop offset="0" stop-color="#0b1230"/>
        <stop offset="1" stop-color="#1b2552"/>
      </linearGradient>
    </defs>
    <polygon points="0,0 610,0 503,203 0,203" fill="url(#navyFade)"/>
    <polyline points="614,-4 506,206 622,418 1040,418" fill="none" stroke="var(--red)" stroke-width="9"/>
    <polyline points="630,-4 522,206 632,406" fill="none" stroke="var(--navy)" stroke-width="5"/>
    <polygon points="0,331 206,331 188,366 0,366" fill="var(--red)"/>
    <polygon points="0,507 634,507 616,568 0,568" fill="var(--navy)"/>
    <polygon points="648,548 1040,548 1040,568 642,568" fill="var(--red)"/>
  </svg>

  <svg class="layer" viewBox="0 0 1040 568" role="img" aria-label="Photo of the company owner with his wife and two children packing boxes on a sofa">
    <defs>
      <linearGradient id="photoTone" x1="0" y1="0" x2="1" y2="1">
        <stop offset="0" stop-color="#e9e4dc"/>
        <stop offset=".5" stop-color="#c9a47a"/>
        <stop offset="1" stop-color="#a97a4e"/>
      </linearGradient>
    </defs>
    <polygon points="640,0 1040,0 1040,402 646,402 538,206" fill="url(#photoTone)"/>
  </svg>

  <svg class="layer" viewBox="0 0 1040 568" aria-hidden="true">
    <polygon points="611,333 1040,333 1040,402 647,402" fill="var(--navy)" fill-opacity=".9"/>
    <polygon points="890,0 1030,0 1030,160 960,146 890,160" fill="var(--red)"/>
    <path d="M897,0 V150 L960,137 L1023,150 V0" fill="none" stroke="var(--white)" stroke-width="1.6" stroke-dasharray="5 4"/>
  </svg>

  <div class="brand"><span class="brand__mark"></span><span class="brand__name">HAUL PIVOT</span></div>

  <div class="contact" style="left:250px;top:18px">
    <p class="contact__lead">Call For FREE Friendly<br>Estimates and Advice!"</p>
    <p class="contact__row"><svg class="contact__icon" viewBox="0 0 16 16"><path d="M3 1l3 3-2 2c1 2 3 4 5 5l2-2 3 3-2 3C7 15 1 9 0 3z" fill="var(--red)"/></svg>858-555-0142</p>
    <p class="contact__row"><svg class="contact__icon" viewBox="0 0 16 16"><rect x="0" y="3" width="16" height="11" fill="var(--red)"/><path d="M0 3l8 6 8-6" fill="none" stroke="#fff" stroke-width="1.4"/></svg>info@haul-pivot.com</p>
    <p class="contact__row"><svg class="contact__icon" viewBox="0 0 16 16"><g fill="none" stroke="var(--red)" stroke-width="1.4"><circle cx="8" cy="8" r="7"/><ellipse cx="8" cy="8" rx="3" ry="7"/><path d="M1 8h14"/></g></svg>www.haul-pivot.com</p>
    <p class="contact__row"><svg class="contact__icon" viewBox="0 0 16 16"><path d="M8 0a5.5 5.5 0 0 0-5.5 5.5C2.5 10 8 16 8 16s5.5-6 5.5-10.5A5.5 5.5 0 0 0 8 0zm0 8a2.5 2.5 0 1 1 0-5 2.5 2.5 0 0 1 0 5z" fill="var(--red)"/></svg>4127 Penwick Lane, Suite B1,<br>San Diego, CA 92177</p>
  </div>

  <h1 class="slogan"><span class="slogan__top" style="display:block">THE MOVING COMPANY</span><span class="slogan__bottom" style="display:block">YOU CAN TRUST AND RELY ON!</span></h1>

  <h2 class="tab" style="left:23px;top:336px">OUR SERVICES</h2>

  <ul class="services" style="left:24px">
    <li><svg class="tick" viewBox="0 0 16 16"><circle cx="8" cy="8" r="8" fill="var(--red)"/><path d="M4.3 8.3l2.5 2.4 4.9-5" fill="none" stroke="#fff" stroke-width="2"/></svg>Packing - Moving - Unpacking</li>
    <li><svg class="tick" viewBox="0 0 16 16"><circle cx="8" cy="8" r="8" fill="var(--red)"/><path d="M4.3 8.3l2.5 2.4 4.9-5" fill="none" stroke="#fff" stroke-width="2"/></svg>Loading - Unloading</li>
    <li><svg class="tick" viewBox="0 0 16 16"><circle cx="8" cy="8" r="8" fill="var(--red)"/><path d="M4.3 8.3l2.5 2.4 4.9-5" fill="none" stroke="#fff" stroke-width="2"/></svg>Storage In Transit</li>
    <li><svg class="tick" viewBox="0 0 16 16"><circle cx="8" cy="8" r="8" fill="var(--red)"/><path d="M4.3 8.3l2.5 2.4 4.9-5" fill="none" stroke="#fff" stroke-width="2"/></svg>Long Term Storage</li>
  </ul>
  <ul class="services" style="left:321px">
    <li><svg class="tick" viewBox="0 0 16 16"><circle cx="8" cy="8" r="8" fill="var(--red)"/><path d="M4.3 8.3l2.5 2.4 4.9-5" fill="none" stroke="#fff" stroke-width="2"/></svg>Local - Long Distance</li>
    <li><svg class="tick" viewBox="0 0 16 16"><circle cx="8" cy="8" r="8" fill="var(--red)"/><path d="M4.3 8.3l2.5 2.4 4.9-5" fill="none" stroke="#fff" stroke-width="2"/></svg>Residential - Commercial</li>
    <li><svg class="tick" viewBox="0 0 16 16"><circle cx="8" cy="8" r="8" fill="var(--red)"/><path d="M4.3 8.3l2.5 2.4 4.9-5" fill="none" stroke="#fff" stroke-width="2"/></svg>Licensed - Insured</li>
    <li><svg class="tick" viewBox="0 0 16 16"><circle cx="8" cy="8" r="8" fill="var(--red)"/><path d="M4.3 8.3l2.5 2.4 4.9-5" fill="none" stroke="#fff" stroke-width="2"/></svg>Free Onsite and Video Estimates</li>
  </ul>

  <p class="licenses" style="left:24px;top:523px;font-size:18px">CAL-T# 574318 | CA# 208751 | MC# 362940 | USDOT# 7140829</p>

  <div class="offer-band">
    <p class="offer-band__main">Free Boxes (*call for details),1 Month Storage Free.</p>
    <p class="offer-band__note">*Offers can not be combined with other offers</p>
  </div>

  <div class="ribbon">
    <p class="ribbon__big">$250 OFF</p>
    <p class="ribbon__small">Long Distance<br>Moves</p>
    <p class="ribbon__stars">★★★</p>
    <p class="ribbon__big">$50 OFF</p>
    <p class="ribbon__small">LOCAL MOVES</p>
  </div>

  <div class="reviews" style="left:654px;top:427px;width:192px;height:83px">
    <div class="reviews__row" style="font-size:15px">Qorvix <span>Tarnly</span><span class="reviews__seal" style="width:50px;height:36px"></span></div>
    <div class="reviews__row" style="font-size:9px;gap:7px">Chatterwall <span>Nestplanner</span><span>Pinbrook</span></div>
  </div>
  <p class="stars" style="left:682px;top:518px;font-size:26px">★★★★★</p>

  <div class="assured" style="left:888px;top:426px">
    <svg class="assured__shield" width="40" height="48" viewBox="0 0 40 48"><path d="M20 0l20 7v15c0 13-9 22-20 26C9 44 0 35 0 22V7z" fill="var(--green)"/></svg>
    <div><p class="assured__name" style="font-size:11px">QORVIX<br>ASSURED</p><p class="assured__sub">Professionals that are licensed,<br>pre-screened, and insured.</p></div>
  </div>
  <svg class="abs" style="left:880px;top:484px" width="58" height="58" viewBox="0 0 58 58" aria-label="Certified HaulSure badge"><circle cx="29" cy="29" r="27" fill="var(--white)" stroke="#2b3a78" stroke-width="3"/></svg>
  <svg class="abs" style="left:962px;top:490px" width="48" height="48" viewBox="0 0 48 48" aria-label="Golden Haul Expert badge"><rect width="48" height="48" fill="var(--orange)"/></svg>
</section>

<!-- BACK -->
<section class="card card--back">
  <svg class="layer" viewBox="0 0 1040 568" aria-hidden="true">
    <defs>
      <linearGradient id="navyFadeBack" x1="0" y1="0" x2="0" y2="1">
        <stop offset="0" stop-color="#0b1230"/>
        <stop offset="1" stop-color="#1b2552"/>
      </linearGradient>
    </defs>
    <polygon points="0,0 478,0 644,279 494,568 0,568" fill="var(--grey)"/>
    <polygon points="0,0 478,0 598,202 0,202" fill="url(#navyFadeBack)"/>
    <polyline points="482,-6 649,279 498,574" fill="none" stroke="var(--navy)" stroke-width="9"/>
    <polyline points="500,-6 666,279 515,574" fill="none" stroke="var(--red)" stroke-width="8"/>
    <polygon points="0,203 172,203 154,239 0,239" fill="var(--red)"/>
    <polygon points="0,529 510,529 490,568 0,568" fill="var(--navy)"/>
  </svg>

  <div class="brand"><span class="brand__mark"></span><span class="brand__name">HAUL PIVOT</span></div>

  <div class="contact" style="left:233px;top:18px">
    <p class="contact__lead">Call For FREE Friendly<br>Estimates and Advice!"</p>
    <p class="contact__row"><svg class="contact__icon" viewBox="0 0 16 16"><path d="M3 1l3 3-2 2c1 2 3 4 5 5l2-2 3 3-2 3C7 15 1 9 0 3z" fill="var(--red)"/></svg>858-555-0142</p>
    <p class="contact__row"><svg class="contact__icon" viewBox="0 0 16 16"><rect x="0" y="3" width="16" height="11" fill="var(--red)"/><path d="M0 3l8 6 8-6" fill="none" stroke="#fff" stroke-width="1.4"/></svg>info@haul-pivot.com</p>
    <p class="contact__row"><svg class="contact__icon" viewBox="0 0 16 16"><g fill="none" stroke="var(--red)" stroke-width="1.4"><circle cx="8" cy="8" r="7"/><ellipse cx="8" cy="8" rx="3" ry="7"/><path d="M1 8h14"/></g></svg>www.haul-pivot.com</p>
    <p class="contact__row"><svg class="contact__icon" viewBox="0 0 16 16"><path d="M8 0a5.5 5.5 0 0 0-5.5 5.5C2.5 10 8 16 8 16s5.5-6 5.5-10.5A5.5 5.5 0 0 0 8 0zm0 8a2.5 2.5 0 1 1 0-5 2.5 2.5 0 0 1 0 5z" fill="var(--red)"/></svg>4127 Penwick Lane, Suite B1,<br>San Diego, CA 92177</p>
  </div>

  <h2 class="tab" style="left:24px;top:207px">ABOUT US</h2>

  <p class="about">Haul Pivot was founded on the belief that moving can be made simple when you have the help and support of an efficient and professional team of movers. It is our goal to provide outstanding customer service at every stage of the process, from the initial call with our moving professionals in the office to the unpacking of your last box. When you are moving with Haul Pivot you can rest assured that we have everything covered. Our team is your team.Haul Pivot is fully licensed and insured and follows all laws and regulations related to moving, employment, vehicle maintenance and otherwise.</p>

  <div class="reviews" style="left:20px;top:424px;width:162px;height:71px;gap:5px;padding:0 8px">
    <div class="reviews__row" style="font-size:13px;gap:8px">Qorvix <span>Tarnly</span><span class="reviews__seal" style="width:42px;height:30px"></span></div>
    <div class="reviews__row" style="font-size:7.5px;gap:5px">Chatterwall <span>Nestplanner</span><span>Pinbrook</span></div>
  </div>
  <p class="stars" style="left:44px;top:497px;font-size:23px">★★★★★</p>

  <div class="assured" style="left:207px;top:440px">
    <svg class="assured__shield" width="40" height="48" viewBox="0 0 40 48"><path d="M20 0l20 7v15c0 13-9 22-20 26C9 44 0 35 0 22V7z" fill="var(--green)"/></svg>
    <div><p class="assured__name" style="font-size:11px">QORVIX<br>ASSURED</p><p class="assured__sub">Professionals that are licensed,<br>pre-screened, and insured.</p></div>
  </div>
  <svg class="abs" style="left:353px;top:436px" width="58" height="58" viewBox="0 0 58 58" aria-label="Certified HaulSure badge"><circle cx="29" cy="29" r="27" fill="var(--white)" stroke="#2b3a78" stroke-width="3"/></svg>
  <svg class="abs" style="left:433px;top:441px" width="48" height="48" viewBox="0 0 48 48" aria-label="Golden Haul Expert badge"><rect width="48" height="48" fill="var(--orange)"/></svg>

  <p class="licenses" style="left:18px;top:539px;font-size:14px">CAL-T# 574318 | CA# 208751 | MC# 362940 | USDOT# 7140829</p>

  <div class="stamp" aria-label="Postage area"></div>
</section>

</body>
</html>
```